Product Description Graphic

We are designing a new product and need a better graphic to describe it.

We are not worried about names of the modules yet but want to be descriptive of capabilities. Right now "Present & CMA" should really be "Presentations & CMA".

I overall like the shape of the triangle and the arrow for Contacts but this is a very unsophisticated graphic done by a non-designer. Also need to better show that each block of capabilites will also have paywall capabilities.

Target Market(s)

Real Estate Brokerage Firms and Real Estate Agents

Industry/Entity Type

Real Estate

Colors

Designer to choose colors to be used in the design.

Requirements
Must have
• Sophisticated design. Paywall description embedded.

```html
<!DOCTYPE html>
<html lang="en">
<head>
<meta charset="utf-8">
<title>Paywall Feature</title>
<link rel="stylesheet" href="https://fonts.googleapis.com/css2?family=Montserrat:wght@600;700;800&display=swap">
<style>
  :root {
    --ink: #0c0c0c;
    --rule: #b9b9b9;
    --blue: #0a72e6;
    --blue-deep: #0b3f86;
    --pink: #ff4d7a;
    --pink-deep: #c10f43;
    --yellow: #fdbd23;
    --yellow-deep: #9c7310;
    --teal: #52dccb;
    --teal-deep: #118676;
    --orange: #ff6e3c;
    --orange-deep: #b33012;
    --paper: #ffffff;
  }
  * { margin: 0; padding: 0; box-sizing: border-box; }
  html, body { width: 1200px; height: 1070px; overflow: hidden; background: var(--paper); }
  .canvas { position: relative; width: 1200px; height: 1070px; font-family: "Montserrat", sans-serif; }
  .title {
    position: absolute; top: 128px; left: 0; width: 1200px; text-align: center;
    font-size: 60px; font-weight: 700; letter-spacing: 6px; color: var(--ink); line-height: 1;
  }
  .dots { position: absolute; top: 225px; left: 0; width: 1200px; display: flex; justify-content: center; gap: 20px; }
  .dots span { width: 14px; height: 14px; border-radius: 50%; }
  .dots .d1 { background: var(--blue); } .dots .d2 { background: var(--pink); }
  .dots .d3 { background: var(--yellow); } .dots .d4 { background: var(--teal); }
  .dots .d5 { background: var(--orange); }
  .chart { position: absolute; top: 0; left: 0; width: 1200px; height: 1074px; }
  .row-label { font-weight: 700; font-size: 19.5px; letter-spacing: 0.4px; }
  .band-label { font-weight: 700; font-size: 19px; letter-spacing: 1px; fill: rgba(255,255,255,0.55); }
  .rule { stroke: var(--rule); stroke-width: 1.2; }
  .icon { fill: none; stroke: #fff; stroke-width: 1.6; stroke-linecap: round; stroke-linejoin: round; }
</style>
</head>
<body>
<div class="canvas">
  <h1 class="title">PAYWALL FEATURE</h1>
  <div class="dots"><span class="d1"></span><span class="d2"></span><span class="d3"></span><span class="d4"></span><span class="d5"></span></div>

  <svg class="chart" viewBox="0 0 1050 940" xmlns="http://www.w3.org/2000/svg">
    <defs>
      <linearGradient id="g-blue" x1="0" x2="1"><stop offset="0" stop-color="var(--blue-deep)"/><stop offset="1" stop-color="var(--blue)"/></linearGradient>
      <linearGradient id="g-pink" x1="0" x2="1"><stop offset="0" stop-color="var(--pink-deep)"/><stop offset="1" stop-color="var(--pink)"/></linearGradient>
      <linearGradient id="g-yellow" x1="0" x2="1"><stop offset="0" stop-color="var(--yellow-deep)"/><stop offset="1" stop-color="var(--yellow)"/></linearGradient>
      <linearGradient id="g-teal" x1="0" x2="1"><stop offset="0" stop-color="var(--teal-deep)"/><stop offset="1" stop-color="var(--teal)"/></linearGradient>
      <linearGradient id="g-orange" x1="0" x2="1"><stop offset="0" stop-color="var(--orange-deep)"/><stop offset="1" stop-color="var(--orange)"/></linearGradient>
      <filter id="soft" x="-20%" y="-200%" width="140%" height="500%"><feGaussianBlur stdDeviation="9"/></filter>
    </defs>

    <!-- row rules -->
    <g class="rules">
      <line class="rule" x1="540" y1="310" x2="924" y2="310"/>
      <line class="rule" x1="600" y1="377" x2="924" y2="377"/>
      <line class="rule" x1="640" y1="470" x2="924" y2="470"/>
      <line class="rule" x1="690" y1="559" x2="924" y2="559"/>
      <line class="rule" x1="730" y1="648" x2="924" y2="648"/>
      <line class="rule" x1="640" y1="747" x2="924" y2="747"/>
    </g>

    <!-- row ribbons -->
    <g class="ribbons">
      <path d="M385,310 L560,310 C530,320 505,350 495,377 L417,377 Z" fill="url(#g-blue)"/>
      <path d="M400,377 L620,377 C585,392 552,430 536,470 L440,470 Z" fill="url(#g-pink)"/>
      <path d="M440,470 L665,470 C630,486 600,525 585,559 L480,559 Z" fill="url(#g-yellow)"/>
      <path d="M480,559 L710,559 C676,576 646,615 632,648 L520,648 Z" fill="url(#g-teal)"/>
      <path d="M520,648 L750,648 C716,666 682,708 666,747 L560,747 Z" fill="url(#g-orange)"/>
    </g>

    <!-- cone shadow -->
    <ellipse cx="370" cy="792" rx="245" ry="22" fill="#000" opacity="0.28" filter="url(#soft)"/>

    <!-- cone bands -->
    <g class="cone">
      <path d="M182,648 L260,808 Q195,800 142,748 Q150,700 182,648 Z" fill="var(--orange)"/>
      <path d="M232,560 L365,820 Q305,818 260,808 L182,648 Z" fill="var(--teal)"/>
      <path d="M285,470 L452,818 Q405,822 365,820 L232,560 Z" fill="var(--yellow)"/>
      <path d="M338,385 L540,798 Q495,812 452,818 L285,470 Z" fill="var(--pink)"/>
      <path d="M385,312 L602,742 Q580,780 540,798 L338,385 Z" fill="var(--blue)"/>
      <path d="M182,648 L190,645 L232,560 L225,563 Z" fill="var(--orange-deep)"/>
      <path d="M232,560 L240,556 L285,470 L278,474 Z" fill="var(--pink-deep)"/>
      <path d="M285,470 L293,467 L338,385 L331,389 Z" fill="var(--yellow-deep)"/>
      <path d="M338,385 L346,380 L385,312 L378,318 Z" fill="var(--blue-deep)"/>
    </g>

    <!-- band labels -->
    <g class="band-labels" text-anchor="middle">
      <text class="band-label" transform="translate(468,560) rotate(63.4)">EMAIL NURTURE PRINT &amp; SOCIAL</text>
      <text class="band-label" transform="translate(386,612) rotate(63.4)">PRESENTATIONS &amp; CMA</text>
      <text class="band-label" transform="translate(314,678) rotate(63.4)">WEBSITES &amp; LEADS</text>
      <text class="band-label" transform="translate(240,718) rotate(63.4)">CONTACTS</text>
      <text class="band-label" transform="translate(180,748) rotate(63.4)">MOBILE</text>
    </g>

    <!-- ribbon icons -->
    <g class="icons">
      <g class="icon" transform="translate(455,343)">
        <path d="M-10,-6 L-10,-16 L10,-16 L10,-6 M-10,-16 L0,-9 L10,-16"/>
        <rect x="-17" y="-6" width="34" height="13" rx="2"/>
        <rect x="-10" y="2" width="20" height="13"/>
        <line x1="-6" y1="7" x2="6" y2="7"/><line x1="-6" y1="11" x2="6" y2="11"/>
      </g>
      <g class="icon" transform="translate(490,422)">
        <rect x="-17" y="-15" width="34" height="26" rx="1"/>
        <line x1="-20" y1="-15" x2="20" y2="-15"/>
        <line x1="0" y1="11" x2="0" y2="18"/><circle cx="0" cy="19" r="1.5"/>
        <line x1="-12" y1="-8" x2="-2" y2="-8"/><line x1="-12" y1="-3" x2="-2" y2="-3"/><line x1="-12" y1="2" x2="-4" y2="2"/>
        <circle cx="7" cy="-1" r="6"/><path d="M7,-7 L7,-1 L12,2"/>
      </g>
      <g class="icon" transform="translate(535,515)">
        <circle cx="-2" cy="-2" r="15"/>
        <ellipse cx="-2" cy="-2" rx="6" ry="15"/>
        <line x1="-17" y1="-2" x2="13" y2="-2"/>
        <path d="M-15,-9 L11,-9 M-15,5 L6,5"/>
        <path d="M6,4 L6,18 L9,15 L12,20 L14,19 L11,14 L15,14 Z" fill="currentColor"/>
      </g>
      <g class="icon" transform="translate(578,603)">
        <rect x="-11" y="-17" width="24" height="34" rx="2"/>
        <line x1="-15" y1="-10" x2="-8" y2="-10"/><line x1="-15" y1="0" x2="-8" y2="0"/><line x1="-15" y1="10" x2="-8" y2="10"/>
        <circle cx="1" cy="-4" r="4"/><path d="M-6,8 Q1,0 8,8"/>
      </g>
      <g class="icon" transform="translate(622,697)">
        <rect x="-13" y="-18" width="20" height="34" rx="3"/>
        <path d="M-7,-10 Q-3,-14 1,-10 M-9,-7 Q-3,-12 3,-7"/>
        <path d="M-3,0 L-3,-6 Q-3,-8 -1,-8 Q1,-8 1,-6 L1,2 L5,0 Q9,0 9,4 L12,12 Q12,18 6,20 L0,20 L-6,12"/>
      </g>
    </g>

    <!-- row labels -->
    <g class="row-labels">
      <text class="row-label" x="585" y="350" fill="var(--blue)">EMAIL NURTURE PRINT &amp; SOCIAL</text>
      <text class="row-label" x="632" y="430" fill="var(--pink)">PRESENTATIONS &amp; CMA</text>
      <text class="row-label" x="656" y="521" fill="var(--yellow)">WEBSITES &amp; LEADS</text>
      <text class="row-label" x="698" y="610" fill="var(--teal)">CONTACTS</text>
      <text class="row-label" x="714" y="712" fill="var(--orange)">MOBILE</text>
    </g>
  </svg>
</div>
</body>
</html>
```